Fashion Design Business Card

I need a new business card designed for a new fashion company. I have attached what I have currently designed. I want it more feminine looking, the logo needs to be gold. I want it simple, feminine and stylish. Please give me some different ideas with the fonts.
Updates

I need to send the design we currently have, as we have worked out the logo.
You also need all of our details
Industry/Entity Type
Fashion
Look and feel
Each slider illustrates characteristics of the customer's brand and the style your logo design should communicate.

```html
<!DOCTYPE html>
<html lang="en">
<head>
<meta charset="utf-8">
<title>Marisol Avery — Business Card</title>
<link rel="stylesheet" href="https://fonts.googleapis.com/css2?family=Cinzel:wght@400;600&family=Marcellus&display=swap">
<style>
  :root {
    --page: #ffffff;
    --card-edge: #d2d2d2;
    --card-light: #fafafa;
    --card-mid: #ececec;
    --card-dark: #dcdcdc;
    --ink-name: #5e5e5e;
    --ink-role: #7a7a7a;
    --ink-value: #555555;
    --ink-label: #9a5a14;
    --gold: #c08a2c;
    --shadow: #6e6e6e;
  }
  html, body {
    margin: 0;
    padding: 0;
    width: 1200px;
    height: 721px;
    overflow: hidden;
    background: var(--page);
  }
  .card {
    position: relative;
    width: 1198px;
    height: 719px;
    border: 1px solid var(--card-edge);
    border-radius: 34px;
    overflow: hidden;
    background:
      radial-gradient(ellipse 70% 80% at 85% 45%, var(--card-light) 0%, transparent 70%),
      linear-gradient(160deg, var(--card-dark) 0%, var(--card-mid) 35%, var(--card-light) 75%, var(--card-mid) 100%);
  }
  .card__backdrop {
    position: absolute;
    inset: 0;
  }
  .brand-mark {
    position: absolute;
    left: 140px;
    top: 158px;
    display: flex;
    align-items: center;
    gap: 10px;
    font-family: "Cinzel", serif;
    font-weight: 600;
    font-size: 34px;
    letter-spacing: 3px;
    color: var(--gold);
  }
  .brand-mark__dot {
    width: 12px;
    height: 12px;
    border-radius: 50%;
    background: var(--gold);
  }
  .identity {
    position: absolute;
    left: 328px;
    top: 160px;
  }
  .identity__name {
    margin: 0;
    font-family: "Cinzel", serif;
    font-weight: 600;
    font-size: 36px;
    line-height: 40px;
    letter-spacing: 7px;
    color: var(--ink-name);
  }
  .identity__role {
    margin: 0;
    font-family: "Marcellus", serif;
    font-size: 28px;
    line-height: 32px;
    letter-spacing: 12.5px;
    color: var(--ink-role);
  }
  .contact {
    position: absolute;
    left: 183px;
    top: 508px;
    margin: 0;
    display: grid;
    grid-template-columns: 148px auto;
    row-gap: 2px;
  }
  .contact__label {
    font-family: "Cinzel", serif;
    font-size: 23px;
    line-height: 32px;
    letter-spacing: 4px;
    color: var(--ink-label);
  }
  .contact__label--lead { font-size: 25px; }
  .contact__value {
    margin: 0;
    font-family: "Marcellus", serif;
    font-size: 25px;
    line-height: 32px;
    letter-spacing: 4px;
    color: var(--ink-value);
  }
  .contact__value--phone { letter-spacing: 5px; }
</style>
</head>
<body>
  <div class="card">
    <svg class="card__backdrop" width="1198" height="719" viewBox="0 0 1198 719" aria-hidden="true">
      <defs>
        <radialGradient id="floor-shadow" cx="50%" cy="50%" r="50%">
          <stop offset="0%" stop-color="var(--shadow)" stop-opacity="0.55"/>
          <stop offset="60%" stop-color="var(--shadow)" stop-opacity="0.25"/>
          <stop offset="100%" stop-color="var(--shadow)" stop-opacity="0"/>
        </radialGradient>
      </defs>
      <ellipse cx="1010" cy="440" rx="290" ry="52" fill="url(#floor-shadow)"/>
    </svg>

    <div class="brand-mark">
      <span class="brand-mark__dot"></span>
      <span class="brand-mark__name">Avery</span>
    </div>

    <div class="identity">
      <h1 class="identity__name">Marisol Avery</h1>
      <p class="identity__role">fashion designer</p>
    </div>

    <dl class="contact">
      <dt class="contact__label contact__label--lead">PH</dt>
      <dd class="contact__value contact__value--phone">0400123456</dd>
      <dt class="contact__label">EMAIL</dt>
      <dd class="contact__value">marisol@marisolavery.com</dd>
      <dt class="contact__label">WEB</dt>
      <dd class="contact__value">www.marisolavery.com</dd>
    </dl>
  </div>
</body>
</html>
```